Professional TRIF0LD or BIFOLD Brochure Design for Tech Company

We would like a professional, modern, clean brochure that lists the products and services we offer.

We would like to have either a trifold or bifold flyer (depending on what looks best) and we would like it to be double sided off course.

Please look at the files that are attached. You will find the text that we want to incorporate and some images of the product that we offer. (all images do not have to be used. it just has to look professional)

Target Market(s)

technology industry

Industry/Entity Type

Information Technology

Font styles to use
Serif

Requirements
Must have
• (I also attached the text so its easier to understand)
• KOPT Tech, LLC.
• 4182 Dunmore Ave.
• Brellton, NV 90572
• Tel: (555)247-6190
• Fax: (555)247-6158
• E-mail: sales@kopttech-sample.com
• ABOUT US
• KOPT Tech, LLC provides Enterprise IT Hardware in the same quality of service and equipment that major brands provide without the major brand pricing.
• We strive to deliver an alternate source for clients to obtain major brand hardware such as Zantor™, QX™, and WJT™ at discounted rates and faster response times. Because the core of Enterprise class equipment revolves around reliability, our on-site testing facility fully examines all equipment to ensure that all hardware shipped and received succeeds industry standards for quality control.
• Our excellent customer service, top grade equipment coupled with our 5-year comprehensive warranty on configured machines allowed us to successfully develop a network of over 18,000 clients ranging from individual IT consultants to Meridale 500 companies. With our dedicated employees and 10,000 square foot warehouse we are able to provide countless configurations of Servers, Storages, and Workstations to businesses worldwide within a 72 hour time-frame. We are confident that we can fulfill all of your IT needs!
• WHY CHOOSE US
• At KOPT Tech, LLC our mission is to be a market leader in providing top tier IT Enterprise Hardware at unmatched prices, supplemented by the best technical support and customer service in the industry.
• Great Customer Service: our dedicated representatives are available 24 hours a day and have strong consumer relationships.
• 5-Year Warranty: KOPT Tech provides 5-year comprehensive warranty on configured machines. Individual components have a 30-day warranty.
• Faster Turn Around: Orders for in-stock items placed on business days before 4:30 PM Pacific Time are typically shipped the same day. KOPT Tech aims to maintain a 24-72 hour shipping time frame.
• Competitive Pricing: You can rest assured that we offer the most competitive prices in the IT industry.
• Custom Configurations: We offer custom configurations on all servers and workstations.
• Technical Support and Repair: KOPT Tech offers technical support and repairs for Zantor and QX servers and workstations.
• Leasing Equipment: KOPT Tech provides the option to lease almost any IT product.
• With our leasing program, you can acquire the latest hardware and software at a manageable cost while remaining flexible as your technology needs grow over time.
• Leasing allows you to pay for your equipment in loan, budgeted payments while retaining your cash for investing in higher return opportunities.
Nice to have
• Please go on our website: kopttech-sample.com and get a feeling of the colors we are interested in.
• We like the vectors that we have in WHY CHOOSE US section
• Please include some of the pictures that we uploaded. As you can see our business focuses on servers and computer hardware. Please include pictures of the computer hardware (you dont need to use all of it- but try to include as much as you can while keeping it clean and professional)

```html
<!DOCTYPE html>
<html lang="en">
<head>
<meta charset="utf-8">
<title>KOPT Tech Trifold Brochure</title>
<link rel="stylesheet" href="https://fonts.googleapis.com/css2?family=Hind:wght@400;600;700&family=Arimo:wght@400;700&display=swap">
<style>
  :root {
    --teal: #2cc3af;
    --teal-dark: #0d6f66;
    --teal-deep: #0a4d49;
    --slate: #5b686d;
    --ink: #4f5457;
    --text: #2f3336;
    --paper: #ffffff;
    --stage: #e6e8e8;
  }
  * { margin: 0; padding: 0; box-sizing: border-box; }
  html, body { width: 792px; height: 1200px; overflow: hidden; background: var(--stage); }
  body { position: relative; font-family: "Arimo", Arial, sans-serif; color: var(--text); }

  .sheet { position: absolute; left: 50px; width: 682px; height: 528px; box-shadow: 0 6px 18px rgba(0,0,0,.25); }
  .sheet--outside { top: 38px; }
  .sheet--inside { top: 613px; }
  .abs { position: absolute; }

  .brand { display: flex; align-items: center; gap: 8px; font-family: "Hind", sans-serif; font-weight: 600; color: var(--teal); letter-spacing: 1px; }
  .brand__mark { background: var(--teal); }

  .panel-teal { background: var(--teal); top: 0; height: 528px; }
  .panel-slate { background: var(--slate); left: 226px; width: 230px; top: 0; height: 528px; }
  .paper { background: var(--paper); }

  .why { left: 15px; top: 15px; width: 196px; height: 497px; padding: 11px 8px 0 13px; }
  .why__title { font-family: "Hind", sans-serif; font-weight: 700; font-size: 18px; color: var(--ink); line-height: 1; margin-bottom: 8px; }
  .why__mission { font-size: 8.2px; font-weight: 700; line-height: 1.42; margin-bottom: 7px; }
  .why__head { font-family: "Hind", sans-serif; font-weight: 700; font-size: 12.5px; color: var(--ink); line-height: 1.2; margin-bottom: 3px; }
  .why__body { font-size: 8.2px; line-height: 1.42; margin-bottom: 7px; }

  .testimonials__title { left: 226px; width: 230px; top: 21px; text-align: center; font-family: "Hind", sans-serif; font-weight: 700; font-size: 17px; color: #fff; }
  .testimonials__quote { left: 246px; width: 190px; top: 52px; text-align: center; font-size: 11.5px; line-height: 1.3; color: var(--teal); }
  .testimonials__by { left: 236px; width: 210px; top: 104px; text-align: center; font-size: 11.5px; line-height: 1.4; color: #fff; }

  .contact-card { left: 243px; top: 199px; width: 196px; height: 313px; }
  .photo { position: absolute; }
  .contact-card__photo { left: 0; top: 0; width: 196px; height: 126px; background: linear-gradient(135deg, #eef2f3, #cdd7db 55%, #f4f6f7); }
  .contact-card__brand { position: absolute; left: 0; width: 196px; top: 126px; height: 94px; justify-content: center; font-size: 20px; }
  .contact-card__rule { position: absolute; left: 0; top: 221px; width: 196px; height: 1px; background: var(--slate); }
  .contact-card__info { position: absolute; left: 0; width: 196px; top: 232px; text-align: center; font-size: 8px; font-weight: 700; line-height: 1.42; font-style: normal; }

  .cover { left: 471px; top: 15px; width: 196px; height: 497px; }
  .cover__brand { position: absolute; left: 0; width: 196px; top: 42px; justify-content: center; font-size: 22px; }
  .cover__url { position: absolute; left: 0; width: 196px; top: 104px; text-align: center; font-size: 8px; letter-spacing: 1.5px; color: var(--ink); }
  .cover__ring { position: absolute; left: 22px; top: 133px; width: 152px; height: 152px; border-radius: 50%; border: 5px solid #e8ecee; }
  .cover__photo { left: 27px; top: 138px; width: 142px; height: 142px; border-radius: 50%; background: radial-gradient(circle at 50% 45%, #9ff0e2, var(--teal) 45%, var(--teal-dark)); }
  .cover__about { position: absolute; left: 8px; top: 327px; width: 179px; height: 108px; background: var(--slate); border-left: 3px solid var(--teal); padding: 9px 7px 0 9px; font-family: "Hind", sans-serif; font-weight: 700; font-size: 12.2px; line-height: 1.3; color: #fff; }
  .cover__phone { position: absolute; left: 27px; top: 460px; font-family: "Hind", sans-serif; font-weight: 700; font-size: 17px; color: var(--slate); line-height: 1; }
  .cover__email { position: absolute; left: 27px; top: 479px; font-size: 8px; color: #7b8487; }

  .inside__field { left: 0; top: 0; width: 456px; height: 528px; background:
      radial-gradient(circle at 62% 62%, rgba(140,240,225,.35), transparent 45%),
      linear-gradient(150deg, #1c8f84 0%, #2cc3af 38%, #147a71 70%, #0b4a45 100%); }
  .inside__right { left: 456px; top: 0; width: 226px; height: 528px; background: var(--paper); }

  .datacenter__photo { left: 15px; top: 16px; width: 186px; height: 120px; background: linear-gradient(90deg, #2d3134, #59636a 30%, #24282b 60%, #6c767c); border: 3px solid #dff5f1; }
  .source { left: 15px; top: 136px; width: 196px; height: 178px; background: rgba(225,248,244,.85); padding: 30px 12px 0 12px; }
  .panel-heading { font-family: "Hind", sans-serif; font-weight: 700; font-size: 17px; line-height: 1.15; color: var(--slate); letter-spacing: -.4px; margin-bottom: 9px; }
  .panel-copy { font-size: 7.9px; line-height: 1.38; color: var(--text); }

  .tower__photo { left: 258px; top: 30px; width: 138px; height: 228px; border-radius: 50% 50% 50% 50% / 30% 30% 30% 30%; background: linear-gradient(160deg, #4a5155, #1e2225 55%, #3a4145); }
  .service { left: 243px; top: 281px; width: 197px; height: 230px; background: rgba(225,248,244,.9); padding: 11px 12px 0 13px; }

  .brand-plate { left: 15px; top: 447px; width: 196px; height: 66px; background: rgba(225,248,244,.3); justify-content: center; font-size: 22px; color: #dff7f3; }
  .brand-plate .brand__mark { background: #dff7f3; }

  .lab__photo { left: 478px; top: 16px; width: 176px; height: 108px; background: linear-gradient(120deg, #f4f6f7, #d9e0e3 50%, #f0f2f3); border-left: 3px solid var(--teal); }
  .leasing { left: 484px; top: 150px; width: 166px; font-family: "Hind", sans-serif; font-weight: 700; font-size: 13px; line-height: 1.3; color: var(--ink); }
  .leasing p + p { margin-top: 9px; }
  .workstations__photo { left: 482px; top: 402px; width: 176px; height: 110px; background: linear-gradient(90deg, #1a8f84, #2c3337 30%, #202629 55%, #3c454a 80%, #2cc3af); }
</style>
</head>
<body>

<section class="sheet sheet--outside">
  <div class="abs panel-teal" style="left:0;width:226px"></div>
  <div class="abs panel-slate"></div>
  <div class="abs panel-teal" style="left:456px;width:226px"></div>

  <article class="abs paper why">
    <h2 class="why__title">WHY CHOOSE US</h2>
    <p class="why__mission">At KOPT Tech, LLC our mission is to be a market leader in providing top tier IT Enterprise Hardware at unmatched prices, supplemented by the best technical support and customer service in the industry.</p>
    <h3 class="why__head">Great Customer Service:</h3>
    <p class="why__body">Our dedicated representatives are available 24 hours a day and have strong consumer relationships.</p>
    <h3 class="why__head">5-Year Warranty:</h3>
    <p class="why__body">KOPT Tech provides 5-year comprehensive warranty on configured machines. Individual components have a 30-day warranty.</p>
    <h3 class="why__head">Faster Turn Around:</h3>
    <p class="why__body">Orders for in-stock items placed on business days before 4:30 PM Pacific Time are typically shipped the same day. KOPT Tech aims to maintain a 24-72 hour shipping time frame.</p>
    <h3 class="why__head">Competitive Pricing:</h3>
    <p class="why__body">You can rest assured that we offer the most competitive prices in the IT industry.</p>
    <h3 class="why__head">Custom Configurations:</h3>
    <p class="why__body">We offer custom configurations on all servers and workstations.</p>
    <h3 class="why__head">Technical Support and Repair:</h3>
    <p class="why__body">KOPT Tech offers technical support and repairs for Zantor and QX servers and workstations.</p>
    <h3 class="why__head">Leasing Equipment:</h3>
    <p class="why__body">KOPT Tech provides the option to lease almost any IT product.</p>
  </article>

  <h2 class="abs testimonials__title">CLIENT TESTIMONIALS</h2>
  <p class="abs testimonials__quote">Perfect unit, and seller happily helped with a specific configuration I needed!</p>
  <p class="abs testimonials__by">— Marcus Ellery<br>(QX W900 Custom<br>Configuration)</p>

  <div class="abs paper contact-card">
    <div class="photo contact-card__photo" role="img" aria-label="Photo of two colleagues reviewing work at a laptop"></div>
    <div class="brand contact-card__brand"><span class="brand__mark" style="width:14px;height:14px"></span>KOPT TECH</div>
    <div class="contact-card__rule"></div>
    <address class="contact-card__info">
      4182 Dunmore Ave.<br>Brellton, NV 90572<br>Tel: (555)247-6190<br>Fax: (555)247-6158<br><br>
      E-mail: sales@kopttech-sample.com<br>www.kopttech-sample.com
    </address>
  </div>

  <div class="abs paper cover">
    <div class="brand cover__brand"><span class="brand__mark" style="width:16px;height:16px"></span>KOPT TECH</div>
    <p class="cover__url">www.kopttech-sample.com</p>
    <div class="cover__ring"></div>
    <div class="abs photo cover__photo" role="img" aria-label="Rack-mount server on a teal glowing background"></div>
    <p class="cover__about">KOPT Tech, LLC provides Enterprise IT Hardware in the same quality of service and equipment that major brands provide without the major brand pricing.</p>
    <svg class="abs" style="left:158px;top:435px" width="52" height="26" viewBox="0 0 52 26" aria-hidden="true"><polygon points="0,0 52,0 26,26" fill="var(--teal)"/></svg>
    <p class="cover__phone">(555)247-6190</p>
    <p class="cover__email">E-mail: sales@kopttech-sample.com</p>
  </div>
</section>

<section class="sheet sheet--inside">
  <div class="abs inside__field" role="img" aria-label="Close-up of a teal circuit board"></div>
  <div class="abs inside__right"></div>

  <div class="abs photo datacenter__photo" role="img" aria-label="Rows of server racks in a data center"></div>
  <article class="abs source">
    <h2 class="panel-heading">We strive to deliver<br>an alternate source</h2>
    <p class="panel-copy">for clients to obtain major brand hardware such as Zantor™, QX™, and WJT™ at discounted rates and faster response times. Because the core of Enterprise class equipment revolves around reliability, our on-site testing facility fully examines all equipment to ensure that all hardware shipped and received succeeds industry standards for quality control.</p>
  </article>
  <svg class="abs" style="left:157px;top:136px" width="54" height="26" viewBox="0 0 54 26" aria-hidden="true"><polygon points="0,0 54,0 27,26" fill="var(--teal)"/></svg>

  <div class="abs photo tower__photo" role="img" aria-label="Tower server shown at an angle"></div>

  <article class="abs service">
    <h2 class="panel-heading">Our excellent<br>customer service,</h2>
    <p class="panel-copy">top grade equipment coupled with our 5-year comprehensive warranty on configured machines allowed us to successfully develop a network of over 18,000 clients ranging from individual IT consultants to Meridale 500 companies. With our dedicated employees and 10,000 square foot warehouse we are able to provide countless configurations of Servers, Storages, and Workstations to businesses worldwide within a 72 hour time-frame. We are confident that we can fulfill all of your IT needs!</p>
  </article>

  <div class="abs brand brand-plate"><span class="brand__mark" style="width:16px;height:16px"></span>KOPT TECH</div>

  <div class="abs photo lab__photo" role="img" aria-label="Technician assembling a desktop computer in a lab"></div>
  <svg class="abs" style="left:616px;top:124px" width="40" height="20" viewBox="0 0 40 20" aria-hidden="true"><polygon points="0,0 40,0 20,20" fill="var(--teal)"/></svg>

  <div class="abs leasing">
    <p>With our leasing program, you can acquire the latest hardware and software at a manageable cost while remaining flexible as your technology needs grow over time.</p>
    <p>Leasing allows you to pay for your equipment in loan, budgeted payments while retaining your cash for investing in higher return opportunities.</p>
  </div>

  <svg class="abs" style="left:482px;top:382px" width="44" height="20" viewBox="0 0 44 20" aria-hidden="true"><polygon points="0,20 44,20 22,0" fill="var(--teal)"/></svg>
  <div class="abs photo workstations__photo" role="img" aria-label="Two tower workstations on a teal background"></div>
</section>

</body>
</html>
```